A5, portrait
Theme is science
audience is VIPS, politicians, executives
this is a really important event, we want a very classy invitation
include logo for bloom and grow and lumen but lumen one bigger
images attached
Have attached some styles we like but doesn't need to be these colours. If we can incorporate some colours from our logo would be good but don't make too colourful and childish

You’re invited to the official opening and launch of Lumen, Centre of Discovery. an industry first, pioneering, STEM hub.

Saturday 30th April, 2022

10:00 am – 12:00 pm

42 Calder Lane, Wrenfield

Light canapes provided. Dress code is smart/casual

All guests will be given a guided walk through of Australia’s first dedicated STEM education hub for children aged 3-6.

Invitation only

RSVP: 18 April to marketing@bloomandgrow.edu.au

```html
<!DOCTYPE html>
<html lang="en">
<head>
<meta charset="utf-8">
<title>Lumen, Centre of Discovery – Launch Invitation</title>
<link rel="stylesheet" href="https://fonts.googleapis.com/css2?family=Crimson+Pro:wght@400;500&family=Montserrat:wght@800&display=swap">
<style>
  :root {
    --page: #ffffff;
    --card: #fdfbfc;
    --ink: #2a2326;
    --gold: #d9c39a;
    --maroon: #6b2034;
    --sky: #1aa7e1;
    --green: #7cc242;
    --red: #e63b3b;
  }
  * { margin: 0; padding: 0; box-sizing: border-box; }
  html, body { width: 800px; height: 1200px; overflow: hidden; background: var(--page); }
  body { position: relative; font-family: "Crimson Pro", Georgia, serif; color: var(--ink); }

  .invitation {
    position: absolute; left: 20px; top: 62px; width: 760px; height: 1075px;
    background:
      radial-gradient(closest-side at 620px 780px, rgba(240,205,215,.35), transparent),
      radial-gradient(closest-side at 180px 260px, rgba(240,215,225,.3), transparent),
      var(--card);
    box-shadow: 0 2px 10px rgba(0,0,0,.12);
    overflow: hidden;
  }
  .gold-frame {
    position: absolute; left: 32px; top: 32px; right: 32px; bottom: 33px;
    border: 1px solid var(--gold);
  }
  .gold-frame::after {
    content: ""; position: absolute; inset: 6px; border: 1px solid var(--gold); opacity: .6;
  }

  .florals { position: absolute; }
  .florals--top {
    left: 40px; top: -60px; width: 760px; height: 200px;
    background:
      radial-gradient(closest-side at 88% 55%, rgba(226,110,145,.75), transparent),
      radial-gradient(closest-side at 60% 45%, rgba(207,198,230,.55), transparent),
      radial-gradient(closest-side at 25% 60%, rgba(185,205,184,.45), transparent);
  }
  .florals--right {
    right: -30px; top: 100px; width: 110px; height: 360px;
    background: radial-gradient(closest-side, rgba(185,205,184,.5), transparent);
  }
  .florals--bottom {
    left: -60px; bottom: -80px; width: 440px; height: 320px;
    background:
      radial-gradient(closest-side at 45% 62%, rgba(207,198,230,.85), transparent),
      radial-gradient(closest-side at 70% 40%, rgba(185,205,184,.45), transparent);
  }

  .centered { position: absolute; left: 0; right: 0; text-align: center; }

  .brand {
    top: 162px; display: flex; justify-content: center; align-items: center; gap: 12px;
  }
  .brand__dot { width: 30px; height: 30px; border-radius: 50%; background: var(--sky); }
  .brand__name {
    font-family: "Montserrat", Arial, sans-serif; font-weight: 800; font-size: 60px;
    letter-spacing: 2px; color: var(--sky); line-height: 1;
  }

  .headline {
    top: 262px; font-family: "Montserrat", Arial, sans-serif; font-weight: 800;
    font-size: 62px; letter-spacing: 3px; line-height: 1; color: var(--sky);
  }

  .intro { top: 342px; font-size: 16.5px; line-height: 21px; }

  .wreath { position: absolute; left: 94px; top: 380px; width: 580px; height: 500px; }
  .wreath__bloom { position: absolute; }
  .wreath__bloom--left {
    left: 20px; top: 130px; width: 140px; height: 230px;
    background:
      radial-gradient(closest-side, rgba(200,35,63,.85), rgba(200,35,63,.35) 55%, transparent);
  }
  .wreath__bloom--top {
    left: 360px; top: 40px; width: 130px; height: 110px;
    background: radial-gradient(closest-side, rgba(170,30,60,.8), rgba(170,30,60,.25) 60%, transparent);
  }
  .wreath__bloom--right {
    left: 390px; top: 260px; width: 150px; height: 200px;
    background: radial-gradient(closest-side, rgba(200,35,63,.85), rgba(230,120,90,.3) 60%, transparent);
  }
  .wreath__bloom--bottom {
    left: 170px; top: 400px; width: 110px; height: 90px;
    background: radial-gradient(closest-side, rgba(200,35,63,.8), rgba(200,35,63,.2) 60%, transparent);
  }
  .wreath__lines { position: absolute; inset: 0; }

  .event-day { top: 502px; font-size: 24px; font-weight: 500; color: var(--sky); }
  .event-date { top: 534px; font-size: 24px; }
  .rule { position: absolute; left: 50%; height: 1px; transform: translateX(-50%); }
  .rule--red { top: 579px; width: 228px; background: var(--red); }
  .rule--red-low { top: 614px; width: 228px; background: var(--red); }
  .rule--green { top: 660px; width: 90px; height: 2px; background: var(--green); }
  .event-time { top: 584px; font-size: 20px; color: var(--red); }
  .event-venue { top: 617px; font-size: 21px; }
  .event-note { top: 676px; font-size: 13.5px; line-height: 17px; }
  .event-extras { top: 738px; font-size: 13.5px; line-height: 17px; color: var(--maroon); }

  .partner {
    top: 890px; display: flex; justify-content: center; align-items: center; gap: 8px;
  }
  .partner__square { width: 22px; height: 22px; background: var(--sky); }
  .partner__name { font-size: 18px; font-weight: 500; color: var(--sky); }

  .exclusive { top: 944px; font-size: 24px; }
  .rsvp {
    position: absolute; left: 230px; top: 984px; width: 300px; height: 22px;
    background: var(--red); color: #fff; font-size: 13px; line-height: 22px; text-align: center;
  }
</style>
</head>
<body>
  <main class="invitation">
    <div class="florals florals--top" role="img" aria-label="Watercolour pink and lilac roses with sage leaves along the top edge"></div>
    <div class="florals florals--right" role="img" aria-label="Trailing sage leaves down the right edge"></div>
    <div class="florals florals--bottom" role="img" aria-label="Watercolour lilac roses with green leaves in the lower left corner"></div>
    <div class="gold-frame"></div>

    <div class="centered brand">
      <span class="brand__dot"></span>
      <span class="brand__name">Lumen</span>
    </div>

    <h1 class="centered headline">INVITATION</h1>

    <p class="centered intro">You’re invited to the official opening and launch of Lumen,<br>Centre of Discovery. An industry first, pioneering, STEM hub.</p>

    <div class="wreath">
      <svg class="wreath__lines" viewBox="0 0 580 500" aria-hidden="true">
        <polygon points="290,20 455,95 488,290 350,460 175,460 70,290 105,95" fill="none" stroke="var(--maroon)" stroke-width="1.4"/>
        <polygon points="250,35 430,60 500,250 420,440 230,485 90,360 80,160" fill="none" stroke="var(--maroon)" stroke-width="1" opacity=".75"/>
      </svg>
      <div class="wreath__bloom wreath__bloom--left" role="img" aria-label="Cluster of red anemones and leaves on the left of the wreath"></div>
      <div class="wreath__bloom wreath__bloom--top" role="img" aria-label="Red blooms at the top right of the wreath"></div>
      <div class="wreath__bloom wreath__bloom--right" role="img" aria-label="Red gerbera and peach leaves at the lower right of the wreath"></div>
      <div class="wreath__bloom wreath__bloom--bottom" role="img" aria-label="Small red blooms at the bottom of the wreath"></div>
    </div>

    <p class="centered event-day">Saturday 30th</p>
    <p class="centered event-date">April, 2022</p>
    <span class="rule rule--red"></span>
    <p class="centered event-time">10:00 am – 12:00 pm</p>
    <span class="rule rule--red-low"></span>
    <p class="centered event-venue">42 Calder Lane, Wrenfield</p>
    <span class="rule rule--green"></span>
    <p class="centered event-note">All guests will be given a guided walk<br>through of Australia’s first dedicated<br>STEM education hub for children aged 3-6.</p>
    <p class="centered event-extras">Light canapés provided.<br>Dress code is smart/casual.</p>

    <div class="centered partner">
      <span class="partner__square"></span>
      <span class="partner__name">Bloom and Grow</span>
    </div>

    <p class="centered exclusive">Invitation only</p>
    <p class="rsvp">RSVP: 18 April to marketing@bloomandgrow.edu.au</p>
  </main>
</body>
</html>
```